Help a start up law firm make an impression! - Website

We are a property development and conveyancing law firm looking for some to design our website. The initial brief is for 6 pages with scope for on-going work.

Law firms are traditionally quite conservative and we want to break the mold. We want to come across as fun and modern, while still being professional.

A good example is https://quorvantlaw.com.au/. It's professional yet modern.
Updates

Another good site I like in the same industry: https://www.tamberwickconveyancing.com.au/

Target Market(s)

Tech savy home buyers and sellers - generally 30 to 50 years old

Industry/Entity Type

Law Firm

Coding

Coded - Design and coding required

Number of Pages Required

5+ page

Font styles to use
Other font styles liked:
• No idea

Colors
f04a50

Requirements
Must have
• The elements set out in the design brief document

```html
<!DOCTYPE html>
<html lang="en">
<head>
<meta charset="utf-8">
<title>Kestrelby Law — Property Law Experts</title>
<link href="https://fonts.googleapis.com/css2?family=Abril+Fatface&family=Roboto:wght@400;500;700&display=swap" rel="stylesheet">
<style>
:root{
  --brand:#d33b5c;
  --brand-dark:#b82d4c;
  --ink:#222226;
  --text:#555;
  --light:#f1f1f1;
  --panel-dark:rgba(12,12,14,.92);
  --white:#fff;
}
*{box-sizing:border-box;margin:0;padding:0}
a{text-decoration:none}
html,body{width:1200px;height:3838px;overflow:hidden}
body{font-family:"Roboto",sans-serif;color:var(--text);background:var(--white);position:relative}
.serif{font-family:"Abril Fatface",serif;letter-spacing:2px}
section,header,nav,footer{position:absolute;left:0;width:1200px}
.btn{display:inline-block;font-family:"Abril Fatface",serif;font-size:15px;letter-spacing:3px;text-transform:uppercase;padding:12px 30px;border:none;text-decoration:none;line-height:1.3}
.btn-brand{background:var(--brand);color:var(--white)}
.btn-white{background:var(--white);color:var(--brand);border:3px solid var(--brand)}
.btn-shadow{box-shadow:4px 4px 0 rgba(0,0,0,.75)}

/* header */
.site-header{top:0;height:67px}
.logo{position:absolute;left:97px;top:10px;font-family:"Abril Fatface",serif;font-size:40px;color:var(--ink);letter-spacing:1px}
.header-phone{position:absolute;right:97px;top:20px;font-family:"Abril Fatface",serif;font-size:24px;color:var(--ink);display:flex;align-items:center;gap:12px}
.main-nav{top:67px;height:41px;background:var(--brand);display:flex;justify-content:space-between;padding:0 97px;align-items:center}
.main-nav a{font-family:"Abril Fatface",serif;color:var(--white);font-size:15px;letter-spacing:1.5px}

/* hero */
.hero{top:108px;height:475px;background:linear-gradient(90deg,#1c1714 0%,#2f2620 40%,#5a4a3e 65%,#3a3640 100%)}
.hero-media{position:absolute;inset:0}
.hero h1{position:absolute;left:97px;top:112px;font-family:"Abril Fatface",serif;font-weight:400;font-size:52px;line-height:1.05;color:var(--white);letter-spacing:3px}
.hero p{position:absolute;left:97px;top:256px;width:420px;font-size:12px;font-weight:700;letter-spacing:1.8px;line-height:1.55;color:var(--white);text-transform:uppercase}
.hero .btn{position:absolute;left:97px;top:304px;width:236px;text-align:center}

/* features */
.features{top:583px;height:410px;background:var(--white)}
.feature{position:absolute;top:103px;width:231px;height:251px;background:#f2f2f2;text-align:center;padding:62px 16px 0}
.feature.active{background:var(--brand);top:88px;height:271px;box-shadow:0 6px 12px rgba(0,0,0,.25)}
.feature .icon{position:absolute;left:50%;top:-40px;transform:translateX(-50%);width:80px;height:80px;border-radius:50%;background:radial-gradient(circle at 40% 35%,#fafafa,#cfcfcf);box-shadow:0 3px 6px rgba(0,0,0,.3);display:flex;align-items:center;justify-content:center}
.feature h3{font-family:"Abril Fatface",serif;font-weight:400;font-size:18px;letter-spacing:1px;color:var(--ink)}
.feature .rule{width:44px;height:3px;background:var(--brand);margin:10px auto 14px}
.feature p{font-size:12.5px;line-height:1.55;color:#444}
.feature.active h3,.feature.active p{color:var(--white)}
.feature.active .rule{background:var(--white)}
.feature .dot{display:block;width:10px;height:10px;border-radius:50%;background:var(--white);border:3px solid #333;margin:10px auto 0}

/* about */
.about{top:993px;height:384px;background:linear-gradient(100deg,#ececec 0%,#f4f4f4 55%,#e2e2e2 100%)}
.section-title{font-family:"Abril Fatface",serif;font-weight:400;color:var(--ink);letter-spacing:3px}
.about h2{position:absolute;left:200px;top:78px;font-size:32px}
.about .rule{position:absolute;left:200px;top:128px;width:50px;height:3px;background:var(--brand)}
.about p{position:absolute;left:200px;top:144px;width:400px;font-size:12.5px;line-height:1.6;color:#444}
.about .btn{position:absolute;left:200px;top:248px;padding:10px 22px;font-size:13px}
.about-photo{position:absolute;left:660px;top:61px;width:410px;height:259px;border:6px solid var(--white);background:linear-gradient(135deg,#c9c1b6,#8c7f74 55%,#4f5a66);box-shadow:0 2px 6px rgba(0,0,0,.2)}

/* conveyancing */
.conveyancing{top:1377px;height:435px}
.conveyancing-photo{position:absolute;inset:0;background:linear-gradient(180deg,#7f8c5e 0%,#c9b47a 35%,#b7905f 60%,#6f6a5e 100%)}
.conveyancing-panel{position:absolute;left:589px;top:61px;width:611px;height:315px;background:rgba(211,59,92,.93);padding:30px 26px}
.conveyancing-panel h2{font-size:30px;color:var(--white)}
.panel-rule{width:50px;height:3px;background:var(--white);margin:10px 0 12px}
.conveyancing-panel p,.development-panel p{font-size:12.5px;line-height:1.65;color:var(--white)}
.conveyancing-panel .btn{margin-top:12px;padding:9px 20px;font-size:13px;border-color:#ddd;color:var(--brand)}

/* cta strip */
.cta-strip{top:1812px;height:166px;display:flex;align-items:center;justify-content:center;gap:34px}
.cta-strip h3{font-family:"Abril Fatface",serif;font-weight:400;font-size:25px;letter-spacing:3px;color:var(--ink)}
.cta-strip .btn{padding:10px 24px;font-size:13px}

/* development */
.development{top:1978px;height:435px}
.development-photo{position:absolute;inset:0;background:linear-gradient(90deg,#c4d3e9 0%,#9eb4d6 40%,#6e7c8e 60%,#a9b8cf 100%)}
.development-panel{position:absolute;left:0;top:62px;width:635px;height:309px;background:var(--panel-dark);padding:30px 97px 0}
.development-panel h2{font-size:30px;color:var(--white);white-space:nowrap}
.development-panel .panel-rule{background:var(--brand)}
.development-panel .btn{margin-top:12px;padding:9px 20px;font-size:13px}

/* blog */
.blog{top:2413px;height:525px;text-align:center}
.blog h2{position:absolute;left:0;width:1200px;top:52px;font-size:29px}
.blog .rule{position:absolute;left:575px;top:100px;width:50px;height:3px;background:var(--brand)}
.blog .lead{position:absolute;left:0;width:1200px;top:120px;font-size:14px;color:#444}
.blog-card{position:absolute;left:97px;top:156px;width:489px;height:307px;background:linear-gradient(160deg,#a9d3ef 0%,#4b8fc6 55%,#13314f 100%);box-shadow:0 3px 8px rgba(0,0,0,.3);text-align:left}
.blog-date{position:absolute;left:0;top:0;width:70px;height:62px;background:var(--brand);color:var(--white);text-align:center;padding-top:8px}
.blog-date strong{display:block;font-family:"Abril Fatface",serif;font-weight:400;font-size:22px}
.blog-date span{font-size:11px}
.blog-caption{position:absolute;left:0;bottom:0;width:100%;height:56px;background:rgba(0,0,0,.55);color:var(--white);font-family:"Abril Fatface",serif;font-size:19px;letter-spacing:1.5px;padding:16px 24px}
.blog-text{position:absolute;left:614px;top:180px;width:490px;text-align:left;font-size:12.5px;line-height:1.65;color:#444}
.blog-meta{position:absolute;left:614px;top:354px;font-size:12px;color:#333;display:flex;gap:8px;align-items:center}
.blog .btn{position:absolute;left:614px;top:394px;padding:10px 22px;font-size:13px}

/* contact */
.contact{top:2938px;height:560px;background:linear-gradient(180deg,#c9b9b0 0%,#9e9790 45%,#4a5863 75%,#6f7c86 100%)}
.contact-panel{position:absolute;left:97px;top:59px;width:1003px;height:440px;background:rgba(14,14,16,.93);text-align:center}
.contact-panel h2{padding-top:40px;font-size:29px;color:var(--white)}
.contact-panel .rule{width:50px;height:3px;background:var(--brand);margin:10px auto 12px}
.contact-panel .lead{font-size:14px;color:var(--white)}
.contact-form{position:absolute;left:87px;top:130px;width:832px}
.field{position:absolute;height:40px;background:var(--white);color:#888;font-size:13px;text-align:left;padding:12px 14px}
.field.message{height:74px}
.contact-form .btn{position:absolute;left:353px;top:256px;padding:8px 16px;font-size:13px}

/* footer */
.site-footer{top:3498px;height:340px;background:var(--brand);color:var(--white)}
.footer-logo{position:absolute;left:97px;top:50px;font-family:"Abril Fatface",serif;font-size:42px;letter-spacing:1px}
.footer-about{position:absolute;left:97px;top:108px;width:400px;font-size:12px;line-height:1.6}
.copyright{position:absolute;left:97px;top:268px;font-size:12px}
.footer-col h4{font-family:"Abril Fatface",serif;font-weight:400;font-size:18px;letter-spacing:2px}
.footer-contact{position:absolute;left:580px;top:52px;width:300px}
.contact-line{display:flex;gap:12px;font-size:11.5px;line-height:1.6;margin-top:14px}
.contact-line svg{flex:none;margin-top:2px}
.footer-hours{position:absolute;left:925px;top:52px;width:200px;font-size:12px;line-height:1.6}
.footer-hours p{margin-top:10px}
.footer-hours h4.social{margin-top:18px}
.social-row{display:flex;gap:12px;margin-top:14px}
.social-row span{width:32px;height:32px;border:1px solid rgba(255,255,255,.6)}
</style>
</head>
<body>

<header class="site-header">
  <div class="logo">Kestrelby Law</div>
  <div class="header-phone">
    <svg width="24" height="24" viewBox="0 0 24 24"><path d="M6.6 10.8a15 15 0 0 0 6.6 6.6l2.2-2.2c.3-.3.7-.4 1-.2 1.1.4 2.3.6 3.6.6.6 0 1 .4 1 1V20c0 .6-.4 1-1 1A17 17 0 0 1 3 4c0-.6.4-1 1-1h3.5c.6 0 1 .4 1 1 0 1.3.2 2.5.6 3.6.1.3 0 .7-.2 1z" fill="#d33b5c"/></svg>
    1-800-555-0147
  </div>
</header>

<nav class="main-nav">
  <a href="#">Home</a><a href="#">About us</a><a href="#">Conveyancing</a><a href="#">Development</a><a href="#">Blog</a><a href="#">Contact us</a>
</nav>

<section class="hero">
  <div class="hero-media" role="img" aria-label="Lawyer in a suit signing documents at a desk"></div>
  <h1>The Property<br>Law Experts</h1>
  <p>Unrivaled response times, fixed fee<br>options and experienced property lawyers</p>
  <a class="btn btn-brand" href="#">Get in touch</a>
</section>

<section class="features">
  <div class="feature" style="left:102px">
    <div class="icon"><svg width="38" height="38" viewBox="0 0 24 24"><path d="M3 12V4h8l10 10-8 8z" fill="#333"/><circle cx="7.5" cy="8" r="1.6" fill="#fff"/></svg></div>
    <h3>Cost Certainty</h3><div class="rule"></div>
    <p>Flexible fee arrangements with no surprises. We offer fixed fee, pay on completion and monthly retainer options to suit your needs.</p>
  </div>
  <div class="feature" style="left:356px">
    <div class="icon"><svg width="38" height="38" viewBox="0 0 24 24"><circle cx="12" cy="7" r="4.5" fill="#333"/><path d="M3 22c0-5 4-8 9-8s9 3 9 8z" fill="#333"/><path d="M12 14l-1.5 3 1.5 5 1.5-5z" fill="#d33b5c"/></svg></div>
    <h3>Expert Lawyers</h3><div class="rule"></div>
    <p>Our experienced team has managed over 2,000 conveyances and worked on some of the most iconic developments in Queensland. All we do is property law, all day everyday.</p>
  </div>
  <div class="feature active" style="left:612px">
    <div class="icon"><svg width="40" height="40" viewBox="0 0 24 24"><path d="M2 12l5-4 5 2 5-2 5 4-6 5-4-3-4 3z" fill="#d33b5c"/></svg></div>
    <h3>Responsive Service</h3><div class="rule"></div>
    <p>The most responsive service, guaranteed. No more waiting days for a lawyer to respond to your email, return your call or prepare your contract.</p>
    <span class="dot"></span>
  </div>
  <div class="feature" style="left:870px">
    <div class="icon"><svg width="38" height="38" viewBox="0 0 24 24"><circle cx="12" cy="7" r="4.5" fill="#333"/><path d="M3 22c0-5 4-8 9-8s9 3 9 8z" fill="#333"/><circle cx="18" cy="5" r="3" fill="none" stroke="#d33b5c" stroke-width="1.5"/></svg></div>
    <h3>Commercial Advice</h3><div class="rule"></div>
    <p>We work with you to get the deal done without legal jargon getting in the way. We understand timing is crucial and we focus on the legal issues that are important to you.</p>
  </div>
</section>

<section class="about">
  <h2 class="section-title">About Us</h2>
  <div class="rule"></div>
  <p>Kestrelby Law is a specialised property development law firm established to assist small to medium property developers with their Queensland developments. We offer a comprehensive service from site acquisition through to conveyancing of finished stock.</p>
  <a class="btn btn-brand btn-shadow" href="#">Read more</a>
  <div class="about-photo" role="img" aria-label="Couple meeting with an adviser in an office"></div>
</section>

<section class="conveyancing">
  <div class="conveyancing-photo" role="img" aria-label="Two-storey suburban home with garage and balcony"></div>
  <div class="conveyancing-panel">
    <h2 class="serif">Conveyancing Services</h2>
    <div class="panel-rule"></div>
    <p>Lorem Ipsum is simply dummy text of the printing and typesetting industry. Lorem Ipsum has been the industry's standard dummy text ever since the 1500s, when an unknown printer took a galley of type and scrambled it to make a type specimen book. It has survived not only five centuries, but also the leap into electronic typesetting, remaining essentially unchanged. It was popularised in the 1960s with the release of Letraset sheets containing Lorem Ipsum passages, and more</p>
    <a class="btn btn-white" href="#">Read more</a>
  </div>
</section>

<section class="cta-strip">
  <h3>Buying or Selling go with the Conveyancing Experts.</h3>
  <a class="btn btn-brand btn-shadow" href="#">Get in touch</a>
</section>

<section class="development">
  <div class="development-photo" role="img" aria-label="Businessman in a suit holding an open book"></div>
  <div class="development-panel">
    <h2 class="serif">Development Law Services</h2>
    <div class="panel-rule"></div>
    <p>Lorem Ipsum is simply dummy text of the printing and typesetting industry. Lorem Ipsum has been the industry's standard dummy text ever since the 1500s, when an unknown printer took a galley of type and scrambled it to make a type specimen book. It has survived not only five centuries, but also the leap into electronic typesetting, remaining essentially unchanged. It was popularised in the 1960s with the release of Letraset sheets containing Lorem Ipsum passages, and more</p>
    <a class="btn btn-white" href="#">Read more</a>
  </div>
</section>

<section class="blog">
  <h2 class="section-title">Recent Blog</h2>
  <div class="rule"></div>
  <p class="lead">It is a long established fact that a reader will be distracted by the readable content of a page when looking at its layout.</p>
  <div class="blog-card" role="img" aria-label="Silhouettes of business people against office windows">
    <div class="blog-date"><strong>20th</strong><span>Sep, 2017</span></div>
    <div class="blog-caption">Real estae laws on the move</div>
  </div>
  <p class="blog-text">There are many variations of passages of Lorem Ipsum available, but the majority have suffered alteration in some form, by injected humour, or randomised words which don't look even slightly believable. If you are going to use a passage of Lorem Ipsum, you need to be sure there isn't anything embarrassing hidden in the middle of text. All the Lorem Ipsum generators on the Internet tend to repeat predefined chunks as necessary, making this the first true generator on the Internet. If you are going to use a passage of Lorem Ipsum.</p>
  <div class="blog-meta"><svg width="14" height="12" viewBox="0 0 14 12"><path d="M1 1h12v7H6l-3 3V8H1z" fill="#d33b5c"/></svg>1 Comment</div>
  <a class="btn btn-brand btn-shadow" href="#">Read more</a>
</section>

<section class="contact" role="img" aria-label="City harbour skyline at dusk">
  <div class="contact-panel">
    <h2 class="section-title">Get in Touch</h2>
    <div class="rule"></div>
    <p class="lead">It is a long established fact that a reader will be distracted by the readable content.</p>
    <div class="contact-form">
      <div class="field" style="left:0;top:0;width:410px">First Name</div>
      <div class="field" style="left:430px;top:0;width:402px">Last Name</div>
      <div class="field" style="left:0;top:58px;width:410px">Email Address</div>
      <div class="field" style="left:430px;top:58px;width:402px">Phone Number</div>
      <div class="field message" style="left:0;top:116px;width:832px">Message</div>
      <a class="btn btn-white" href="#">Get in touch</a>
    </div>
  </div>
</section>

<footer class="site-footer">
  <div class="footer-logo">Kestrelby Law</div>
  <p class="footer-about">There are many variations of passages of Lorem Ipsum available, but the majority have suffered alteration in some form, by injected humour, or randomised words which don't look even slightly believable. There are many variations of passages of Lorem Ipsum available, but the majority have suffered alteration in some form, by injected humour, or randomised words which don't look even slightly believable.</p>
  <p class="copyright">© 2017 &nbsp;|&nbsp; All Rights Reserved.</p>

  <div class="footer-col footer-contact">
    <h4>Contact us</h4>
    <div class="contact-line"><svg width="12" height="16" viewBox="0 0 12 16"><path d="M6 0a6 6 0 0 1 6 6c0 4-6 10-6 10S0 10 0 6a6 6 0 0 1 6-6z" fill="#fff"/><circle cx="6" cy="6" r="2" fill="#d33b5c"/></svg><div>Vantrell &amp; Hoske Corporate<br>Suite 4410 Harbour Lane<br>Brisbane QLD</div></div>
    <div class="contact-line"><svg width="14" height="14" viewBox="0 0 24 24"><path d="M6.6 10.8a15 15 0 0 0 6.6 6.6l2.2-2.2c.3-.3.7-.4 1-.2 1.1.4 2.3.6 3.6.6.6 0 1 .4 1 1V20c0 .6-.4 1-1 1A17 17 0 0 1 3 4c0-.6.4-1 1-1h3.5c.6 0 1 .4 1 1 0 1.3.2 2.5.6 3.6.1.3 0 .7-.2 1z" fill="#fff"/></svg><div>Corporate Office: 1-800-555-0193<br>Tax Services: 1-800-555-0162<br>International: 1-800-555-0178</div></div>
    <div class="contact-line"><svg width="14" height="12" viewBox="0 0 14 12"><rect x="0" y="0" width="14" height="12" fill="#fff"/><path d="M0 0l7 6 7-6" fill="none" stroke="#d33b5c" stroke-width="1.5"/></svg><div>sales@vantrellhoske.com<br>support@vantrellhoske.com<br>office@vantrellhoske.com</div></div>
  </div>

  <div class="footer-col footer-hours">
    <h4>Business Hours</h4>
    <p>Monday-Friday: 7am – 7pm<br>Saturday: 10am – 5pm<br>Sunday: 12pm – 4pm</p>
    <h4 class="social">Social Links</h4>
    <div class="social-row"><span></span><span></span><span></span><span></span></div>
  </div>
</footer>

</body>
</html>
```